Statement of Professional Excellence

Our school community has create a statement of Professional Excellence at our school (TLS = The Linden School at Marrowby) This will be shared internally and with candidates interviewing at our school. We'd like a branded graphic that lists in an interesting way our statements:

Professional Excellence at TLS

We honor the whole child while embracing them where they are.
We are mission-driven individuals whose dedication to our students motivates our daily work.
We bring flexible thinking to allow the needs of the students to drive the learning.
We are patient, nurturing, empathetic, and compassionate people.
We value, trust, and support each other.
We learn and we teach.
We lean into and celebrate diversity.
We build trust through genuine partnerships with families.
We are quirky, fun and proud of it.

```html
<!DOCTYPE html>
<html lang="en">
<head>
<meta charset="utf-8">
<title>Professional Excellence at TLS</title>
<link rel="stylesheet" href="https://fonts.googleapis.com/css2?family=Lora:wght@400;600&display=swap">
<style>
  :root {
    --navy: #1f3347;
    --ink: #1c2530;
    --gold: #e3c35a;
    --gold-deep: #c9a43a;
    --gold-shadow: #b89330;
    --paper: #ffffff;
    --photo-warm: #b88a62;
    --photo-cool: #3d5a7a;
  }
  * { margin: 0; padding: 0; box-sizing: border-box; }
  html, body { width: 849px; height: 1200px; overflow: hidden; background: var(--paper); }
  .poster {
    position: relative;
    width: 849px;
    height: 1200px;
    background: var(--paper);
    overflow: hidden;
    font-family: "Lora", Georgia, serif;
  }
  .decor { position: absolute; inset: 0; width: 849px; height: 1200px; }
  .brand {
    position: absolute;
    top: 44px;
    right: 38px;
    display: flex;
    align-items: center;
    gap: 14px;
    color: var(--navy);
    font-family: "Lora", Georgia, serif;
    font-weight: 400;
  }
  .brand-mark {
    width: 34px; height: 34px;
    border-radius: 50%;
    background: var(--navy);
    flex: none;
  }
  .brand-name {
    font-size: 30px;
    line-height: 1.12;
    text-align: left;
    letter-spacing: 0.5px;
  }
  .statement {
    position: absolute;
    left: 87px;
    top: 246px;
    width: 520px;
  }
  .statement-title {
    font-weight: 600;
    font-size: 29px;
    color: var(--navy);
    margin-bottom: 22px;
    letter-spacing: 0.2px;
  }
  .values { list-style: none; }
  .values li {
    font-size: 20px;
    line-height: 27px;
    color: var(--ink);
    margin-bottom: 21px;
  }
  .photo {
    position: absolute;
    inset: 0;
    width: 849px;
    height: 1200px;
  }
</style>
</head>
<body>
  <main class="poster">
    <svg class="decor" viewBox="0 0 849 1200" aria-hidden="true">
      <defs>
        <linearGradient id="photoTone" x1="0" y1="0" x2="1" y2="1">
          <stop offset="0" stop-color="var(--photo-warm)"/>
          <stop offset="0.55" stop-color="#8a6c55"/>
          <stop offset="1" stop-color="var(--photo-cool)"/>
        </linearGradient>
      </defs>
      <!-- top-left corner bands -->
      <polygon points="0,0 180,0 0,215" fill="var(--navy)"/>
      <polygon points="0,145 135,45 135,165 0,280" fill="var(--gold)"/>
      <polygon points="0,280 135,165 135,195 0,310" fill="var(--gold-shadow)" opacity="0.35"/>

      <!-- right side chevrons -->
      <polygon points="849,205 849,300 760,390 668,390" fill="var(--gold)"/>
      <polygon points="668,390 760,390 849,478 849,575" fill="var(--gold-deep)"/>
      <polygon points="760,480 849,395 849,600 790,600" fill="var(--gold)"/>

      <!-- bottom-right frame -->
      <polygon points="780,660 849,660 849,1200 190,1200" fill="var(--navy)"/>
      <polygon points="790,620 849,620 849,690 770,690" fill="var(--gold)"/>
    </svg>

    <svg class="photo" viewBox="0 0 849 1200" role="img" aria-label="Photo of a teacher leaning over a young boy helping him write at a classroom desk">
      <polygon points="849,690 849,1185 235,1185 840,690" fill="url(#photoTone)"/>
    </svg>

    <div class="brand">
      <span class="brand-mark"></span>
      <span class="brand-name">The Linden School<br>at Marrowby</span>
    </div>

    <section class="statement">
      <h1 class="statement-title">Professional Excellence at TLS</h1>
      <ul class="values">
        <li>We honor the whole child while<br>embracing them where they are.</li>
        <li>We are mission-driven individuals whose<br>dedication to our students motivates<br>our daily work.</li>
        <li>We bring flexible thinking to allow the<br>needs of the students to drive the learning.</li>
        <li>We are patient, nurturing, empathetic,<br>&nbsp;and compassionate people.</li>
        <li>We value, trust, and support each other.<br>We learn and we teach.</li>
        <li>We lean into and celebrate diversity.</li>
        <li>We build trust through genuine<br>partnerships with families.</li>
        <li>We are quirky, fun and proud of it.</li>
      </ul>
    </section>
  </main>
</body>
</html>
```